Professional violinist needs business cards

I am trying to attract the following jobs:
-private violin lessons (primarily classical)
-performance gigs (weddings, birthday parties, funerals, etc.)
-collaborations with other artists (studio recordings, performances)

I want to communicate that I have a very high standard of excellence for my work, but I also love people and celebrations.
Values/style words I like are:
love, joy, peace, fun, beauty, authenticity, excellence, warmth, refined/sleek, free spirited. If that's too confusing, just ignore :)

I will attach my favorite business card template that I could find on Canva. The lines are supposed to be like a music staff, which I think is really cool, but I also don't want it to look too busy. I like the simple black and white--I think it looks sharp--but I also am open to other ideas. I also have seen business cards with pictures included that looked great, so I attached an image that could be used as well.

I am also attaching a file that I made of my initials that could be used as a logo, but I'm not sure if it should be included.

Information on the card:
-My name (18 letters total)
-"violinist"
-phone number, email, website

Thank you!

```html
<!DOCTYPE html>
<html lang="en">
<head>
<meta charset="UTF-8">
<title>Violinist Business Card</title>
<link href="https://fonts.googleapis.com/css2?family=Archivo+Black&family=Questrial&display=swap" rel="stylesheet">
<style>
  :root {
    --page-bg: #f9f9f9;
    --card-white: #ffffff;
    --card-border: #e2e2e2;
    --ink: #111111;
    --accent-yellow: #faf79c;
    --back-black: #000000;
    --staff-white: #ffffff;
    --emblem-light: #ffffff;
    --emblem-shade: #cfcfcf;
    --photo-top: #6f6656;
    --photo-bottom: #3b342b;
  }
  * { margin: 0; padding: 0; box-sizing: border-box; }
  html, body { width: 1200px; height: 1200px; overflow: hidden; }
  body {
    background: var(--page-bg);
    font-family: "Questrial", sans-serif;
    color: var(--ink);
    position: relative;
  }
  .side-label {
    position: absolute;
    top: 190px;
    width: 444px;
    text-align: center;
    font-size: 24px;
    letter-spacing: 0.5px;
  }
  .side-label--front { left: 110px; }
  .side-label--back { left: 663px; }

  .card {
    position: absolute;
    top: 230px;
    width: 444px;
    height: 776px;
    border-radius: 37px;
    overflow: hidden;
  }
  .card--front {
    left: 110px;
    background: var(--card-white);
    border: 1.5px solid var(--card-border);
  }
  .card--back {
    left: 663px;
    background: var(--back-black);
  }

  .portrait {
    position: absolute;
    left: 0; top: 0;
    width: 100%;
    height: 388px;
    background: linear-gradient(180deg, var(--photo-top), var(--photo-bottom));
  }
  .accent-bar {
    position: absolute;
    left: 85px;
    top: 383px;
    width: 272px;
    height: 5px;
    background: var(--accent-yellow);
  }

  .contact-row {
    position: absolute;
    left: 73px;
    display: flex;
    align-items: center;
    gap: 30px;
  }
  .contact-icon {
    width: 43px;
    height: 43px;
    border-radius: 11px;
    background: var(--accent-yellow);
    display: flex;
    align-items: center;
    justify-content: center;
    flex-shrink: 0;
  }
  .contact-icon svg { width: 24px; height: 24px; }
  .contact-text { font-size: 17.5px; line-height: 19px; }
  .person-name {
    font-family: "Archivo Black", sans-serif;
    font-size: 20.5px;
    line-height: 24px;
    letter-spacing: 0.2px;
  }
  .person-role { font-size: 19.5px; line-height: 24px; }

  .row-name { top: 442px; }
  .row-phone { top: 511px; }
  .row-email { top: 578px; }
  .row-web { top: 645px; }

  .staff {
    position: absolute;
    left: 0; top: 0;
    width: 444px;
    height: 776px;
  }
  .emblem {
    position: absolute;
    left: 163px;
    top: 248px;
    width: 124px;
    height: 280px;
    border-radius: 50% 50% 46% 46% / 22% 22% 20% 20%;
    background: radial-gradient(ellipse at 50% 55%, var(--emblem-light) 0%, var(--emblem-light) 35%, var(--emblem-shade) 100%);
    opacity: 0.92;
  }
</style>
</head>
<body>
  <div class="side-label side-label--front">FRONT</div>
  <div class="side-label side-label--back">BACK</div>

  <section class="card card--front">
    <div class="portrait" role="img" aria-label="Photo of the violinist holding her violin and bow in front of a stone wall"></div>
    <div class="accent-bar"></div>

    <div class="contact-row row-name">
      <div class="contact-icon">
        <svg viewBox="0 0 24 24"><circle cx="12" cy="8" r="4.5" fill="#111"/><path d="M3.5 21c0-5 3.8-8 8.5-8s8.5 3 8.5 8z" fill="#111"/></svg>
      </div>
      <div>
        <div class="person-name">NAME SURNAME</div>
        <div class="person-role">Violinist</div>
      </div>
    </div>

    <div class="contact-row row-phone">
      <div class="contact-icon">
        <svg viewBox="0 0 24 24"><rect x="6" y="1.5" width="12" height="21" rx="2" fill="#111"/><rect x="7.8" y="4.5" width="8.4" height="13.5" fill="#faf79c"/><circle cx="12" cy="20.2" r="1" fill="#faf79c"/></svg>
      </div>
      <div class="contact-text">+1 (555) 014 2345<br>+1 (555) 014 2345</div>
    </div>

    <div class="contact-row row-email">
      <div class="contact-icon">
        <svg viewBox="0 0 24 24"><rect x="1.5" y="5" width="21" height="14" rx="1.5" fill="#111"/><path d="M2.5 6.5 12 13l9.5-6.5" fill="none" stroke="#faf79c" stroke-width="1.5"/></svg>
      </div>
      <div class="contact-text">hello@ariastrings.com</div>
    </div>

    <div class="contact-row row-web">
      <div class="contact-icon">
        <svg viewBox="0 0 24 24" fill="none" stroke="#111" stroke-width="1.3"><circle cx="12" cy="12" r="10.5"/><circle cx="12" cy="12" r="7"/><ellipse cx="12" cy="12" rx="3" ry="7"/><path d="M5 12h14M6 8.5h12M6 15.5h12"/></svg>
      </div>
      <div class="contact-text">www.ariastrings.com</div>
    </div>
  </section>

  <section class="card card--back">
    <svg class="staff" viewBox="0 0 444 776">
      <g stroke="#ffffff" stroke-width="1.6">
        <line x1="0" y1="281" x2="444" y2="281"/>
        <line x1="0" y1="312" x2="444" y2="312"/>
        <line x1="0" y1="344" x2="444" y2="344"/>
        <line x1="0" y1="375" x2="444" y2="375"/>
        <line x1="0" y1="407" x2="444" y2="407"/>
        <line x1="0" y1="438" x2="444" y2="438"/>
        <line x1="0" y1="469" x2="444" y2="469"/>
        <line x1="0" y1="500" x2="444" y2="500"/>
      </g>
    </svg>
    <div class="emblem" role="img" aria-label="White emblem combining a treble clef and a violin silhouette on the music staff"></div>
  </section>
</body>
</html>
```